The name of the company is Dorvane Holdings, LLC. I would like a business card with a logo.

On the top left, I would like a logo design of a crown and I would like Dorvane over the top of the crown while Investments on the bottom. Please see attached files as an example of crown and positioning of Dorvane Holdings. Then I would like the letters DH in the middle(see picture).

Colors

Designer to choose colors to be used in the design.

```html
<!DOCTYPE html>
<html lang="en">
<head>
<meta charset="UTF-8">
<title>Dorvane Holdings, LLC — Business Card</title>
<link href="https://fonts.googleapis.com/css2?family=Roboto:wght@400;500;700&display=swap" rel="stylesheet">
<style>
  :root {
    --backdrop: #2b2b2b;
    --card-dark: #262626;
    --card-light: #f1f1ef;
    --brand-green: #2ea84a;
    --ink: #1e1e1e;
    --mark-fill: #3fae4d;
    --mark-ghost: rgba(220, 200, 120, 0.16);
  }
  * { margin: 0; padding: 0; box-sizing: border-box; }
  html, body {
    width: 1200px; height: 960px; overflow: hidden;
    background: var(--backdrop);
    font-family: "Roboto", Arial, sans-serif;
  }
  .sheet {
    position: relative; width: 1200px; height: 960px;
    display: flex; flex-direction: column; align-items: center;
    justify-content: center; gap: 36px;
  }
  .card {
    position: relative; width: 760px; height: 430px;
    border-radius: 28px; overflow: hidden;
  }
  .card--back { background: var(--card-dark); }
  .card--front { background: var(--card-light); }

  .brand-lockup {
    display: flex; flex-direction: column; align-items: center; gap: 14px;
    color: var(--brand-green); font-weight: 500; text-align: center;
  }
  .brand-lockup__dot {
    border-radius: 50%; background: var(--mark-fill);
  }
  .card--back .brand-lockup {
    position: absolute; left: 50%; top: 50%; transform: translate(-50%, -50%);
  }
  .card--back .brand-lockup__dot { width: 130px; height: 130px; }
  .card--back .brand-lockup__name { font-size: 40px; letter-spacing: 1px; }

  .card--front .brand-lockup {
    position: absolute; left: 46px; top: 40px;
  }
  .card--front .brand-lockup__dot { width: 74px; height: 74px; }
  .card--front .brand-lockup__name { font-size: 20px; }

  .ghost-mark {
    position: absolute; right: -40px; top: 130px;
    width: 300px; height: 300px; border-radius: 50%;
    background: var(--mark-ghost);
  }

  .person {
    position: absolute; right: 50px; top: 44px; text-align: right;
  }
  .person__name { color: var(--brand-green); font-weight: 700; font-size: 30px; }
  .person__role { color: var(--ink); font-size: 19px; margin-top: 4px; }

  .contact {
    position: absolute; left: 46px; bottom: 40px; color: var(--ink);
    font-size: 20px; line-height: 1.35;
  }
  .contact__company { color: var(--brand-green); font-weight: 500; }
  .contact__line { display: flex; align-items: center; gap: 10px; }
  .contact__line svg { width: 16px; height: 16px; flex: none; }
  .contact__address { margin-bottom: 6px; }
</style>
</head>
<body>
  <main class="sheet">
    <section class="card card--back" aria-label="Card back">
      <div class="brand-lockup">
        <span class="brand-lockup__dot"></span>
        <span class="brand-lockup__name">Dorvane Holdings, LLC</span>
      </div>
    </section>

    <section class="card card--front" aria-label="Card front">
      <div class="ghost-mark" aria-hidden="true"></div>

      <div class="brand-lockup">
        <span class="brand-lockup__dot"></span>
        <span class="brand-lockup__name">Dorvane Holdings, LLC</span>
      </div>

      <div class="person">
        <div class="person__name">Soren Dorvane</div>
        <div class="person__role">Founder/CEO</div>
      </div>

      <div class="contact">
        <div class="contact__company">Dorvane Holdings, LLC</div>
        <div class="contact__address">418 Larchmere Road, suite 200<br>Westbrook Hills CA, 90417</div>
        <div class="contact__line">
          <svg viewBox="0 0 16 16" aria-hidden="true"><path fill="#2ea84a" d="M3.5 1.5l2.4 2.6-1.3 1.7c.9 2 2.4 3.6 4.5 4.6l1.7-1.3 2.7 2.4-1.5 2.3C6.7 13.5 2.5 9.3 1.2 3z"/></svg>
          <span>(555) 014-2290</span>
        </div>
        <div class="contact__line">
          <svg viewBox="0 0 16 16" aria-hidden="true"><rect x="1" y="3" width="14" height="10" fill="#2ea84a"/><path d="M1.5 3.5L8 9l6.5-5.5" fill="none" stroke="#f1f1ef" stroke-width="1.4"/></svg>
          <span>dorvane.holdings@mailnest.com</span>
        </div>
      </div>
    </section>
  </main>
</body>
</html>
```